Flat Belly Design Graphics for Social

I want to create 9 social media graphics (new Instagram size 4:5 (1080 x 1350 pixels) focusing on our Flat Belly Graphics, using the pics attached. Use the attached pics, NO RANDOM STOCK PHOTOGRAPHY. For the color scheme of the graphics, the color palette is attached. YOU MUST POST ALL 9 GRAPHICS IN ONE ENTRY.
Using the 3 titles below, create one set of graphics. 1) with all text, then for the others, use the pictures as detailed below in IMPORTANT:
1. 21-Night Lean Middle Reboot Beyond 50
2. The 20-Second Trim-Core Menu Guide
3. Starlet Tricks to a Slender Midline Beyond 50 - Zero Scalpel Needed
IMPORTANT:
Only use RK Pic 1 and RK Pic 2 with the title, 21-Night Lean Middle Reboot Beyond 50
Only use meal plan1 and meal plan2 pics with the title, 20-Second Trim-Core Menu Guide
Only use starlet tricks 1 and starlet tricks 2 pics with the title, Starlet Tricks to a Slender Midline Beyond 50 - Zero Scalpel Needed
women over 40

```html
<!DOCTYPE html>
<html lang="en">
<head>
<meta charset="utf-8">
<title>21-Night Lean Middle Reboot – Social Set</title>
<link rel="stylesheet" href="https://fonts.googleapis.com/css2?family=Bebas+Neue&family=Caveat:wght@600&family=Dancing+Script:wght@700&family=Lato:wght@700;900&display=swap">
<style>
  :root{
    --board:#58585a;
    --blush:#fde9ee;
    --rose:#e39bb2;
    --pine:#2b4a45;
    --white:#ffffff;
    --photo-a:#e8d7cf;
    --photo-b:#a07766;
    --food-a:#e7b4a0;
    --food-b:#8fa86a;
  }
  *{margin:0;padding:0;box-sizing:border-box}
  html,body{width:1200px;height:904px;overflow:hidden;background:var(--board)}
  .board{position:relative;width:1200px;height:904px}
  .post{position:absolute;overflow:hidden;background:var(--blush)}
  .post--hero{left:35px;top:30px;width:442px;height:557px}
  .post--tile{width:218px;height:273px}
  .c1{left:490px}.c2{left:723px}.c3{left:954px}
  .r1{top:28px}.r2{top:314px}.r3{top:598px}
  .abs{position:absolute}
  .display{font-family:"Bebas Neue",Impact,sans-serif;line-height:.86;white-space:nowrap}
  .sans{font-family:Lato,Arial,sans-serif;font-weight:900;line-height:1.05;white-space:nowrap}
  .script{font-family:"Dancing Script",cursive;font-weight:700;white-space:nowrap}
  .hand{font-family:Caveat,cursive;font-weight:600;white-space:nowrap}
  .pink{color:var(--rose)}.green{color:var(--pine)}.white{color:var(--white)}
  .center{text-align:center}
  .vertical{transform-origin:left top;transform:rotate(-90deg)}
  .photo-person{background:linear-gradient(160deg,var(--photo-a),var(--photo-b))}
  .photo-duo{background:linear-gradient(180deg,#f3ece8 0%,#c9a08e 55%,var(--blush) 100%)}
  .photo-food{background:linear-gradient(135deg,var(--food-a),#d8c28a 50%,var(--food-b))}
  .disc{position:absolute;border-radius:50%;background:var(--rose)}
</style>
</head>
<body>
<main class="board">

  <!-- Hero: 21-Night Lean Middle Reboot -->
  <section class="post post--hero">
    <div class="disc" style="left:-90px;top:-190px;width:420px;height:568px"></div>
    <div class="abs photo-person" role="img" aria-label="Smiling woman in a white cropped sweater pointing at her flat stomach" style="left:234px;top:178px;width:208px;height:379px;border-radius:100px 100px 0 0"></div>
    <div class="abs display white" style="left:22px;top:26px;font-size:182px">21</div>
    <div class="abs display white vertical" style="left:176px;top:172px;font-size:92px">NIGHT</div>
    <div class="abs display white" style="left:30px;top:186px;font-size:120px">LEAN</div>
    <div class="abs display white" style="left:30px;top:290px;font-size:64px">MIDDLE</div>
    <div class="abs sans green" style="left:28px;top:440px;font-size:34px;line-height:1.15">REBOOT<br>BEYOND 50</div>
  </section>

  <!-- Tile: 20-Second menu guide, outline numeral -->
  <section class="post post--tile c1 r1">
    <div class="abs photo-food" role="img" aria-label="Chicken, berries, grains and vegetables in bowls" style="left:0;top:0;width:218px;height:58px"></div>
    <div class="abs photo-food" role="img" aria-label="Potatoes, asparagus and chickpeas" style="left:0;top:58px;width:34px;height:150px"></div>
    <div class="abs photo-food" role="img" aria-label="Nuts and a meal plan note card" style="left:190px;top:58px;width:28px;height:150px"></div>
    <svg class="abs" style="left:64px;top:62px" width="110" height="100" viewBox="0 0 110 100">
      <text x="55" y="96" text-anchor="middle" font-family="Bebas Neue, sans-serif" font-size="132" fill="none" stroke="var(--pine)" stroke-width="1.2">20</text>
    </svg>
    <div class="abs display green" style="left:44px;top:146px;font-size:22px">THE</div>
    <div class="abs display pink" style="left:42px;top:165px;font-size:50px">SECOND</div>
    <div class="abs sans green center" style="left:0;width:218px;top:212px;font-size:19px">TRIM-CORE<br>MENU GUIDE</div>
  </section>

  <!-- Tile: Starlet tricks, photo top -->
  <section class="post post--tile c2 r1">
    <div class="abs photo-duo" role="img" aria-label="Two women sharing a whispered secret, one looking delighted" style="left:0;top:0;width:218px;height:140px"></div>
    <div class="abs sans green center" style="left:0;width:218px;top:128px;font-size:15px">STARLET<br>TRICKS TO A</div>
    <div class="abs display pink center" style="left:0;width:218px;top:168px;font-size:37px">SLENDER MIDLINE</div>
    <div class="abs script green center" style="left:0;width:218px;top:198px;font-size:24px">Beyond 50</div>
    <div class="abs sans pink center" style="left:0;width:218px;top:245px;font-size:10.5px;font-weight:700">ZERO SCALPEL NEEDED</div>
  </section>

  <!-- Tile: 21-Night with band and wave -->
  <section class="post post--tile c3 r1">
    <div class="abs photo-person" role="img" aria-label="Smiling woman in a white cropped sweater showing her waist" style="left:110px;top:0;width:108px;height:240px"></div>
    <div class="abs" style="left:0;top:108px;width:110px;height:38px;background:var(--rose)"></div>
    <div class="abs display pink" style="left:12px;top:18px;font-size:112px">21</div>
    <div class="abs display green" style="left:22px;top:112px;font-size:38px">NIGHT</div>
    <div class="abs display green" style="left:16px;top:152px;font-size:48px">LEAN</div>
    <div class="abs display green" style="left:16px;top:192px;font-size:30px">MIDDLE</div>
    <svg class="abs" style="left:0;top:222px" width="218" height="51" viewBox="0 0 218 51">
      <path d="M0 10 Q70 -4 140 10 T218 8 V51 H0 Z" fill="var(--rose)"/>
    </svg>
    <div class="abs script white" style="left:16px;top:236px;font-size:20px">Reboot Beyond 50</div>
  </section>

  <!-- Tile: Starlet tricks, text top with disc -->
  <section class="post post--tile c1 r2">
    <div class="abs photo-duo" role="img" aria-label="Two women, one whispering a secret to the other" style="left:96px;top:92px;width:122px;height:181px;background:linear-gradient(180deg,var(--blush),#c99a86 60%,#8fb1c9)"></div>
    <div class="abs sans green center" style="left:0;width:218px;top:12px;font-size:16px">STARLET<br>TRICKS TO A</div>
    <div class="abs display pink center" style="left:0;width:218px;top:50px;font-size:38px">SLENDER MIDLINE</div>
    <div class="disc" style="left:8px;top:112px;width:82px;height:82px"></div>
    <div class="abs script white center" style="left:8px;width:82px;top:122px;font-size:20px;line-height:1">Beyond<br><span style="font-size:32px">50</span></div>
    <div class="abs sans green center" style="left:8px;width:82px;top:210px;font-size:11.5px;font-weight:700;line-height:1.2">ZERO<br>SCALPEL<br>NEEDED</div>
  </section>

  <!-- Tile: 21-Night with vertical NIGHT and disc -->
  <section class="post post--tile c2 r2">
    <div class="abs photo-person" role="img" aria-label="Woman in a sheer black top smiling down at her waist" style="left:124px;top:0;width:94px;height:273px;background:linear-gradient(160deg,var(--photo-a),#3a2d2a)"></div>
    <div class="abs display pink" style="left:8px;top:16px;font-size:96px">21</div>
    <div class="abs display pink vertical" style="left:84px;top:96px;font-size:40px">NIGHT</div>
    <div class="abs display green" style="left:10px;top:100px;font-size:60px">LEAN</div>
    <div class="abs display green" style="left:10px;top:150px;font-size:28px">MIDDLE</div>
    <div class="disc" style="left:14px;top:183px;width:76px;height:76px"></div>
    <div class="abs sans white center" style="left:14px;width:76px;top:197px;font-size:12.5px;font-weight:700;line-height:1.1">REBOOT<br>BEYOND<br>50</div>
  </section>

  <!-- Tile: 20-Second notebook over food -->
  <section class="post post--tile c3 r2">
    <div class="abs photo-food" role="img" aria-label="Colourful frame of vegetables, fruit, fish and lentils" style="left:0;top:0;width:218px;height:273px"></div>
    <div class="abs" style="left:44px;top:62px;width:130px;height:150px;background:var(--white);transform:rotate(-4deg);box-shadow:0 2px 6px rgba(0,0,0,.2)">
      <div class="disc" style="left:62px;top:8px;width:56px;height:56px"></div>
      <div class="abs display white center" style="left:62px;width:56px;top:15px;font-size:44px">20</div>
      <div class="abs display green" style="left:16px;top:50px;font-size:18px">THE</div>
      <div class="abs display green" style="left:16px;top:68px;font-size:32px">SECOND</div>
      <div class="abs sans pink" style="left:16px;top:98px;font-size:13px;font-weight:700">TRIM-CORE</div>
      <div class="abs hand green" style="left:16px;top:112px;font-size:22px">MENU GUIDE</div>
    </div>
  </section>

  <!-- Tile: 21-Night headline top -->
  <section class="post post--tile c1 r3">
    <div class="abs photo-person" role="img" aria-label="Smiling woman in a white cropped sweater pointing at her stomach" style="left:32px;top:92px;width:110px;height:181px;border-radius:55px 55px 0 0"></div>
    <div class="abs display pink center" style="left:0;width:218px;top:14px;font-size:56px">21 NIGHT</div>
    <div class="abs display green center" style="left:0;width:218px;top:64px;font-size:34px">LEAN MIDDLE</div>
    <div class="disc" style="left:146px;top:108px;width:64px;height:64px"></div>
    <div class="abs sans white center" style="left:146px;width:64px;top:118px;font-size:11px;font-weight:700;line-height:1.1">REBOOT<br>BEYOND<br>50</div>
  </section>

  <!-- Tile: 20-Second framed -->
  <section class="post post--tile c2 r3">
    <div class="abs photo-food" role="img" aria-label="Chicken, grains, berries and vegetables" style="left:0;top:0;width:218px;height:28px"></div>
    <div class="abs photo-food" role="img" aria-label="Asparagus, meal plan card and grains" style="left:0;top:28px;width:38px;height:190px"></div>
    <div class="abs photo-food" role="img" aria-label="Nuts and chickpeas" style="left:190px;top:28px;width:28px;height:190px"></div>
    <div class="abs photo-food" role="img" aria-label="Berries, butter and raw chicken in bowls" style="left:0;top:218px;width:218px;height:55px"></div>
    <div class="abs" style="left:42px;top:32px;width:142px;height:182px;border:1px solid var(--rose)"></div>
    <div class="abs display green center" style="left:86px;width:54px;top:24px;font-size:22px;background:var(--blush)">THE</div>
    <div class="abs display pink" style="left:50px;top:58px;font-size:108px">20</div>
    <div class="abs display pink vertical" style="left:142px;top:158px;font-size:40px">SECOND</div>
    <div class="abs sans green center" style="left:43px;width:140px;top:165px;font-size:17px;background:var(--blush)">TRIM-CORE<br>MENU GUIDE</div>
  </section>

  <!-- Tile: Starlet tricks, disc bottom -->
  <section class="post post--tile c3 r3">
    <div class="abs photo-duo" role="img" aria-label="Two women sharing a whispered secret" style="left:0;top:0;width:218px;height:140px"></div>
    <div class="disc" style="left:39px;top:104px;width:141px;height:141px"></div>
    <div class="abs sans white center" style="left:39px;width:141px;top:114px;font-size:10px;font-weight:700">STARLET<br>TRICKS TO A</div>
    <div class="abs display white center" style="left:39px;width:141px;top:140px;font-size:34px;line-height:.9">SLENDER<br>MIDLINE</div>
    <div class="abs script green center" style="left:39px;width:141px;top:206px;font-size:18px">Beyond 50</div>
    <div class="abs sans green center" style="left:0;width:218px;top:252px;font-size:10.5px;font-weight:700">ZERO SCALPEL NEEDED</div>
  </section>

</main>
</body>
</html>
```